Korlane Email Signature Banners – Fabrication Capability Series

www.Korlane.com.au is an Australian engineering and fabrication company specialising in fabrication and welding of :
steel piping spools,
skids and frames,
small volume process steel tanks
and general steel fabrication
We require four distinct banner designs for use in Velnor Tidmark email signatures. Each banner will highlight a specific capability while maintaining a consistent brand identity.
Deliverables
Four banners total:
Piping Spools Fabrication – focus on precision welding and stainless steel pipework
Skid & Frames Fabrication – highlight skid systems and structural frames
Small Steel Tanks Fabrication – show fabricated tanks and workshop craftsmanship
General Fabrication Solutions – broad steel fabrication theme for company-wide use
Dimensions: 600–700 px wide × 100 px high
Format: PNG (preferred), small file size prefered
Resolution: 72 dpi
Background: non-transparent, industrial or workshop setting
Text examples:
1. Piping Spools Fabrication
Option A: “Expert Fabrication Solutions for Process Piping”
Option B: “Precision Welding for Complex Systems”
Option C: “Delivering Quality in Every Spool”
Option D: “Engineered for Flow, Built for Strength”
2. Skid & Frames Fabrication
Option A: “Custom Engineered Modular Systems”
Option B: “Built Strong. Designed Smart.”
Option C: “Reliable Frames for Industrial Performance”
Option D: “Modular Fabrication for Seamless Integration”
3. Small Steel Tanks Fabrication
Option A: “Precision Built for Your Needs”
Option B: “Compact Strength. Proven Durability.”
Option C: “Fabricated for Performance and Longevity”
Option D: “Small Tanks. Big Reliability.”
4. General Fabrication Solutions
Option A: “Quality Craftsmanship, Proven Results”
Option B: “Your Partner in Precision Fabrication”
Option C: “Engineering Excellence in Every Weld”
Option D: “Australian Fabrication. Global Standards.”
Style Direction
Clean, professional, and engineering‑focused
Use Korlane brand colours
Blend photo realism with vector clarity (no heavy gradients)
Include subtle industrial textures or workshop imagery
Typography: bold sans‑serif, legible at small scale
Usage Context
These banners will appear at the bottom of staff email signatures via Tidmark Email Signature Tool for Velnor 365, so clarity and fast loading are essential. No Logo is required in the banners.
Reference
Existing Korlane signature is attached. Colour palette to match the signature style and logo.
Target Market(s)
Engineering and construction companies,
Industry/Entity Type
Engineering fabrication design
Look and feel

```html
<!DOCTYPE html>
<html lang="en">
<head>
<meta charset="utf-8">
<title>Korlane Email Signature Banners – Fabrication Capability Series</title>
<link rel="stylesheet" href="https://fonts.googleapis.com/css2?family=Poppins:wght@700&display=swap">
<style>
  :root {
    --canvas-bg: #ededed;
    --accent-blue: #29a8e2;
    --headline-white: #ffffff;
    --steel-deep: #052536;
    --steel-mid: #0d4a69;
    --steel-light: #1c6f96;
    --steel-haze: #4f7f93;
    --spark-glow: #9fb4b8;
    --steel-night: #020f18;
  }
  * { margin: 0; padding: 0; box-sizing: border-box; }
  html, body {
    width: 1200px;
    height: 876px;
    overflow: hidden;
    background: var(--canvas-bg);
  }
  .banner-series {
    position: relative;
    width: 1200px;
    height: 876px;
  }
  .banner {
    position: absolute;
    left: 113px;
    width: 974px;
    height: 163px;
    overflow: hidden;
  }
  .banner--general { top: 81px; }
  .banner--tanks   { top: 265px; }
  .banner--skids   { top: 449px; }
  .banner--spools  { top: 633px; }

  .banner__photo {
    position: absolute;
    inset: 0;
  }
  .banner--general .banner__photo {
    background:
      radial-gradient(ellipse 150px 70px at 505px 150px, rgba(159,180,184,0.75), transparent 70%),
      radial-gradient(ellipse 330px 150px at 520px 110px, rgba(79,127,147,0.55), transparent 75%),
      radial-gradient(ellipse 120px 40px at 490px 10px, rgba(159,180,184,0.35), transparent 70%),
      linear-gradient(180deg, transparent 70%, rgba(28,111,150,0.5) 100%),
      linear-gradient(90deg, var(--steel-mid) 0%, var(--steel-light) 40%, var(--steel-mid) 72%, var(--steel-deep) 92%, var(--steel-night) 100%);
  }
  .banner--tanks .banner__photo {
    background:
      linear-gradient(180deg, rgba(79,127,147,0.45) 0%, rgba(28,111,150,0.2) 28%, transparent 45%),
      radial-gradient(ellipse 240px 90px at 650px 70px, rgba(79,127,147,0.45), transparent 75%),
      radial-gradient(ellipse 200px 60px at 880px 30px, rgba(159,180,184,0.3), transparent 75%),
      linear-gradient(180deg, transparent 60%, rgba(2,15,24,0.45) 100%),
      linear-gradient(90deg, var(--steel-mid) 0%, var(--steel-light) 30%, var(--steel-mid) 60%, var(--steel-light) 85%, var(--steel-mid) 100%);
  }
  .banner--skids .banner__photo {
    background:
      radial-gradient(ellipse 90px 55px at 510px 25px, rgba(159,180,184,0.7), transparent 70%),
      radial-gradient(ellipse 380px 70px at 600px 95px, rgba(79,127,147,0.45), transparent 75%),
      radial-gradient(ellipse 120px 90px at 930px 70px, rgba(2,15,24,0.5), transparent 75%),
      linear-gradient(90deg, var(--steel-mid) 0%, var(--steel-light) 35%, var(--steel-mid) 65%, var(--steel-deep) 100%);
  }
  .banner--spools .banner__photo {
    background:
      radial-gradient(ellipse 110px 60px at 620px 65px, rgba(79,127,147,0.55), transparent 70%),
      radial-gradient(ellipse 280px 163px at 640px 90px, rgba(13,74,105,0.85), transparent 75%),
      radial-gradient(ellipse 90px 70px at 560px 150px, rgba(159,180,184,0.25), transparent 70%),
      linear-gradient(90deg, var(--steel-night) 0%, var(--steel-deep) 40%, var(--steel-mid) 62%, var(--steel-deep) 82%, var(--steel-night) 100%);
  }

  .banner__headline {
    position: absolute;
    left: 56px;
    top: 50px;
    padding-left: 12px;
    border-left: 4.5px solid var(--accent-blue);
    font-family: 'Poppins', sans-serif;
    font-weight: 700;
    font-size: 33px;
    line-height: 38px;
    letter-spacing: -0.3px;
    color: var(--headline-white);
    white-space: nowrap;
  }
  .banner__line { display: block; margin-top: -6px; margin-bottom: -6px; }
  .banner__highlight { color: var(--accent-blue); }
</style>
</head>
<body>
<main class="banner-series">

  <section class="banner banner--general">
    <div class="banner__photo" role="img" aria-label="Close-up of a welding torch throwing sparks across a steel workpiece, blue duotone"></div>
    <h2 class="banner__headline">
      <span class="banner__line">Engineering <span class="banner__highlight">Excellence</span></span>
      <span class="banner__line">in Every Weld</span>
    </h2>
  </section>

  <section class="banner banner--tanks">
    <div class="banner__photo" role="img" aria-label="Workshop floor stacked with large steel pipes and fabricated cylinders, blue duotone"></div>
    <h2 class="banner__headline">
      <span class="banner__line">Compact Strength</span>
      <span class="banner__line banner__highlight">Proven Durability</span>
    </h2>
  </section>

  <section class="banner banner--skids">
    <div class="banner__photo" role="img" aria-label="Welding a steel pipe assembly on a workshop frame beside a welding machine, blue duotone"></div>
    <h2 class="banner__headline">
      <span class="banner__line">Custom <span class="banner__highlight">Engineered</span></span>
      <span class="banner__line">Modular Systems</span>
    </h2>
  </section>

  <section class="banner banner--spools">
    <div class="banner__photo" role="img" aria-label="Welder in protective gear working amid sparks in a dark workshop, blue duotone"></div>
    <h2 class="banner__headline">
      <span class="banner__line">Expert <span class="banner__highlight">Fabrication Solutions</span></span>
      <span class="banner__line">for Process Piping</span>
    </h2>
  </section>

</main>
</body>
</html>
```